Redesign criminal justice consulting website

We run a small professional services firm that does research, evaluation, consulting, and training on criminal justice issues. We need to redesign our website (www.brvolquest.com). The existing site is something we made ourselves. It is unprofessional and does not do a good job of communicating what we do or who we are.

We would like the new site to provide a basic overview of what we do. Moreover, we would like it to communicate several themes that represent who we are:

* global

* innovative

* analytical

* practical

We view the principal design challenge as figuring out a subtle, interesting, and graphically appealing way to communicate these themes.

Target Market(s)

Our primary customers are governments, research firms, criminal justice agencies, and schools. The people who we want to find our site are seeking research, evaluation, training, or consulting services related to crime, criminal justice, or policing.

Industry/Entity Type

Consulting

Number of Pages Required

2 pages

Requirements
Must have
• 1. We would like the site to use our logo. It is attached (please use the maroon 4-color version with the company name but without the slogan). The site should also use the colors present in our logo. It may use other colors as well, as long as these colors coordinate with the logo colors.

• 2. For main pages or buttons, we need the following:
• *Home
• *About BVQ
• *Services
• *E-Training
• *Resources
• *Contact BVQ

• 3. We like simple, crisp, subtle designs over "busier," cluttered, or very complex designs.

• 4. We'd like to receive, at a minimum, the home page and a sample inner page.
Nice to have
• We need some help in thinking through what regions or sections should exist on the home page. We are thinking about having a window on there where we can make announcements about recent developments like new reports, new e-training videos, new photographs, etc... We are open to suggestions here.
Should not have
• 1. Gimmicky or overused clipart.
• 2. Cliched images associated with criminal justice, including magnifying glasses, scales of justice, etc... Our logo makes a subtle nod to criminal justice through the use of a fingerprint as the dot on the "J" in the company initials. That''s sufficient for our purposes. Concentrate instead on the themes listed above.
• 3. Major use of colors that don't match our logo, like blue.

```html
<!DOCTYPE html>
<html lang="en">
<head>
<meta charset="utf-8">
<title>BVQ – Brvolquest Analysts</title>
<link rel="stylesheet" href="https://fonts.googleapis.com/css2?family=Roboto:wght@300;400;700&family=Roboto+Condensed:wght@300;400;700&display=swap">
<style>
:root{
  --orange:#d8380a;
  --maroon:#a02f14;
  --ink:#111;
  --text:#555;
  --page:#f0efed;
  --band:#e4e4e4;
  --panel:#ffffff;
  --soft:#f8f8f8;
  --black:#000;
}
*{margin:0;padding:0;box-sizing:border-box}
html,body{width:1200px;height:2973px;overflow:hidden}
body{position:relative;background:var(--page);font-family:"Roboto",Arial,sans-serif;color:var(--text)}
.abs{position:absolute}
.header{left:0;width:1200px;height:146px;background:#fff}
.brand{left:54px;display:flex;align-items:center;gap:14px;color:var(--maroon);font-family:"Roboto",Arial,sans-serif;font-weight:700}
.brand-dot{width:22px;height:22px;border-radius:50%;background:var(--maroon)}
.brand-initials{font-size:62px;line-height:1;letter-spacing:-1px}
.brand-name{font-size:20px;letter-spacing:2px;text-transform:uppercase;line-height:1.25}
.rule{left:0;width:1200px;height:9px;background:#e6e6e6}
.nav{left:0;width:1200px;height:50px;background:var(--orange);border-bottom:1px solid #b72e06}
.nav-item{position:absolute;top:7px;width:181px;height:43px;display:flex;align-items:center;justify-content:center;color:#fff;font-family:"Roboto Condensed",Arial,sans-serif;font-weight:700;font-size:12.5px;letter-spacing:.8px;text-transform:uppercase}
.nav-item.active{background:var(--black)}
.nav-item.active::after{content:"";position:absolute;left:50%;bottom:-11px;margin-left:-10px;border-left:10px solid transparent;border-right:10px solid transparent;border-top:11px solid var(--black)}
.hero-band{left:0;width:1200px;background:var(--band)}
.hero{left:54px;top:222px;width:1086px;height:363px;background:var(--black);overflow:hidden}
.hero-photo{position:absolute;right:0;top:0;width:492px;height:363px;background:linear-gradient(200deg,#f2f2f2 0%,#cfcfcf 35%,#7a2a22 55%,#111 80%)}
.hero-copy{position:absolute;left:61px;top:100px;width:560px;color:#fff}
.hero-copy h1{font-family:"Roboto",Arial,sans-serif;font-weight:700;font-size:38px;line-height:1}
.hero-copy h2{font-weight:700;font-size:22px;margin-top:18px}
.hero-copy p{font-weight:700;font-size:13px;line-height:16px;margin-top:14px}
.panel{left:54px;width:1086px;background:var(--panel);border-bottom:6px solid #dcdcdc}
.col{position:absolute;width:310px}
.col-soft{background:var(--soft)}
.col-title{font-family:"Roboto Condensed",Arial,sans-serif;font-weight:400;font-size:27px;color:var(--ink);letter-spacing:-.5px;line-height:1}
.col-title em{font-style:normal;color:var(--orange)}
.thumb{display:block;width:303px;height:159px;margin-top:22px}
.lead{font-weight:700;font-size:17px;color:var(--ink);margin-top:22px;line-height:20px}
.body-copy{font-weight:300;font-size:16px;line-height:19px;margin-top:12px}
.more{display:block;font-weight:700;font-size:16px;color:var(--orange);margin-top:22px}
.bullets{list-style:none;margin-top:38px}
.bullets li{font-weight:700;font-size:16px;color:var(--orange);line-height:28px}
.bullets li::before{content:"»";color:#777;font-weight:400;margin-right:14px}
.footer{left:0;width:1200px;height:76px;background:var(--band);display:flex;align-items:center;justify-content:center;font-family:"Roboto Condensed",Arial,sans-serif;font-size:12px;letter-spacing:.8px;text-transform:uppercase;color:#777}
.footer b{font-weight:700;margin-right:6px}
.divider{left:0;width:1200px;background:var(--black)}
.inner-title{font-family:"Roboto Condensed",Arial,sans-serif;font-size:27px;color:var(--orange);line-height:1}
.team-photo{left:115px;top:1847px;width:370px;height:248px;background:linear-gradient(160deg,#e9e9e4 0%,#c9c6bd 40%,#3a3430 70%,#d8d6d0 100%)}
.about-text{left:513px;top:1850px;width:560px}
.about-text .strong{font-weight:700;font-size:17px;line-height:19px;color:#444}
.about-text p{font-weight:300;font-size:16px;line-height:19px;margin-top:19px}
.about-note{left:115px;top:2110px;font-weight:700;font-size:17px;color:#444}
.long-copy{left:115px;top:2247px;width:945px}
.long-copy p{font-weight:300;font-size:16px;line-height:19px;margin-bottom:22px}
.long-copy p.gap{margin-top:34px}
</style>
</head>
<body>

<!-- HOME PAGE -->
<header class="abs header" style="top:0">
  <div class="abs brand" style="top:36px"><span class="brand-dot"></span><span class="brand-initials">BVQ</span><span class="brand-name">Brvolquest<br>Analysts</span></div>
</header>
<div class="abs rule" style="top:146px"></div>
<nav class="abs nav" style="top:155px">
  <span class="nav-item active" style="left:54px">Home</span>
  <span class="nav-item" style="left:235px">About BVQ</span>
  <span class="nav-item" style="left:416px">Services</span>
  <span class="nav-item" style="left:596px">E-Training</span>
  <span class="nav-item" style="left:778px">Resources</span>
  <span class="nav-item" style="left:959px">Contact BVQ</span>
</nav>
<div class="abs hero-band" style="top:205px;height:365px"></div>
<section class="abs hero">
  <div class="hero-photo" role="img" aria-label="Open hardcover book with a red ribbon bookmark"></div>
  <div class="hero-copy">
    <h1>What we do?</h1>
    <h2>This is what we’re asked by many people.</h2>
    <p>Our clients know we suscipit nibh nisl vel enim ad duis vero ut at, dolore in eum dolore magna zzril ut, consequat ex feugiat, quis, nostrud ea, vel.</p>
  </div>
</section>

<main class="abs panel" style="top:603px;height:770px">
  <div class="col" style="left:50px;top:60px">
    <h3 class="col-title">Whats <em>new!</em></h3>
    <div class="thumb" role="img" aria-label="Stack of folded newspapers" style="background:linear-gradient(170deg,#f4f4f4,#cfc8c4 60%,#eee)"></div>
    <p class="lead">Vel vulputate nulla et duis amet.</p>
    <p class="body-copy">Exerci nulla, in ipsum esse in ut, wisi nulla consequat eu wisi eum tincidunt vel nostrud.</p>
    <ul class="bullets">
      <li>Exerci nulla</li>
      <li>In ipsum esse in</li>
      <li>Wisi nulla consequat</li>
      <li>Eu wisi eum</li>
      <li>Tincidunt vel nostrud.</li>
    </ul>
  </div>
  <div class="col col-soft" style="left:372px;top:27px;width:337px;height:716px;padding:33px 0 0 18px">
    <h3 class="col-title">Vel vulputate!</h3>
    <div class="thumb" role="img" aria-label="Fountain pen resting on a printed line chart" style="background:linear-gradient(160deg,#d9d9d9,#f6f6f6 45%,#bfa98a 100%)"></div>
    <p class="lead">Vel vulputate nulla et duis amet.</p>
    <p class="body-copy" style="width:310px">Exerci nulla, in ipsum esse in ut, wisi nulla consequat eu wisi eum tincidunt vel nostrud.</p>
    <p class="body-copy" style="margin-top:19px">Eu wisi eum tincidunt vel nostrud.</p>
    <p class="body-copy" style="margin-top:19px;width:310px">Augue in laoreet, euismod nostrud iusto vel amet wisi iusto quis duis feugiat adipiscing ut. Lobortis, lobortis velit erat dolore qui.</p>
    <p class="body-copy" style="margin-top:19px;width:300px">Wisi iusto quis duis feugiat adipiscing ut. Lobortis, lobortis velit erat dolore qui.</p>
    <p class="body-copy" style="margin-top:19px;width:230px">Blandit sit elit minim blandit ullamcorper.</p>
    <span class="more">read more...</span>
  </div>
  <div class="col" style="left:736px;top:68px">
    <p class="lead" style="margin-top:0">Vel vulputate nulla et duis amet.</p>
    <p class="body-copy">Exerci nulla, in ipsum esse in ut, wisi nulla consequat eu wisi eum tincidunt vel nostrud.</p>
    <p class="body-copy" style="margin-top:19px;width:270px">Exerci nulla, in ipsum esse in ut, wisi nulla consequat eu wisi eum suscipit tincidunt vel nostrud at vulputate vel illum molestie minim minim consequat.</p>
    <p class="body-copy" style="margin-top:19px;width:250px">Augue in laoreet, euismod nostrud iusto vel amet wisi iusto</p>
    <p class="body-copy" style="margin-top:19px;width:312px">Quis duis feugiat adipiscing ut. Lobortis, lobortis velit erat dolore qui, blandit sit elit minim blandit ullamcorper.</p>
    <p class="body-copy" style="margin-top:19px;width:300px">Augue in laoreet, euismod nostrud iusto vel amet wisi iusto quis duis feug adipiscing ut. Lobortis, lobortis velit er dolore qui.</p>
    <p class="body-copy" style="margin-top:19px;width:230px">Blandit sit elit minim blandit ullamcorper.</p>
    <span class="more">read more...</span>
  </div>
</main>
<footer class="abs footer" style="top:1365px"><b>Copyright |</b> All rights reserved</footer>

<div class="abs divider" style="top:1440px;height:91px"></div>

<!-- ABOUT PAGE -->
<header class="abs header" style="top:1531px">
  <div class="abs brand" style="top:36px"><span class="brand-dot"></span><span class="brand-initials">BVQ</span><span class="brand-name">Brvolquest<br>Analysts</span></div>
</header>
<div class="abs rule" style="top:1677px"></div>
<nav class="abs nav" style="top:1686px">
  <span class="nav-item" style="left:54px">Home</span>
  <span class="nav-item active" style="left:235px">About BVQ</span>
  <span class="nav-item" style="left:416px">Services</span>
  <span class="nav-item" style="left:596px">E-Training</span>
  <span class="nav-item" style="left:778px">Resources</span>
  <span class="nav-item" style="left:959px">Contact BVQ</span>
</nav>

<main class="abs panel" style="top:1752px;height:1143px"></main>
<h2 class="abs inner-title" style="left:115px;top:1802px">About us</h2>
<div class="abs team-photo" role="img" aria-label="Three colleagues reviewing documents around a laptop in a bright office"></div>
<div class="abs about-text">
  <p class="strong" style="margin-top:0">Consequat in feugiat eros duis amet, te, blandit, odio duis te illum aliquip duis aliquam consequat quis, diam vero.</p>
  <p>Exerci nulla, dolor lorem esse in facilisi, ut nulla consequat eu wisi eum ullamcorper euismod autem quis facilisis vulputate vel vel esse ad minim commodo.</p>
  <p>Autem, feugait enim minim vero commodo accumsan delenit ut illum sed vero, hendrerit ut suscipit velit vel, ullamcorper aliquip ea.</p>
  <p>Qui ea eum duis duis blandit dolor accumsan exerci enim nulla dignissim dolore aliquam nulla nibh et velit dolore aliquip consequat wisi ut.</p>
</div>
<p class="abs about-note">Ut in luptatum dolore dolor ullamcorper et molestie in laoreet, euismod nostrud.</p>

<h2 class="abs inner-title" style="left:115px;top:2198px">Vel duis</h2>
<div class="abs long-copy">
  <p>Vel duis, tincidunt feugait hendrerit iriure ipsum delenit, iriure, odio lobortis veniam, enim luptatum facilisi nulla volutpat. Elit, qui vel facilisis duis eu veniam duis, facilisi dolor feugiat, aliquip, ad lobortis, nonummy. Adipiscing amet, ut consectetuer nibh nostrud sed commodo esse, lobortis dolore praesent odio dolore, accumsan, iusto quis facilisis. Qui ea eum duis duis blandit dolor accumsan exerci enim nulla dignissim dolore aliquam nulla nibh et velit dolore aliquip consequat wisi ut. Duis autem te suscipit volutpat tation velit praesent eum magna, ipsum elit in consectetuer ut hendrerit exerci zzril. Lorem veniam molestie vero eros enim eu vulputate, ut eros nulla ea. Autem, feugait enim minim vero commodo accumsan delenit ut illum sed vero, hendrerit ut suscipit velit vel, ullamcorper aliquip ea.</p>
  <p>Praesent laoreet, euismod nostrud et vel sit ut iusto quis augue feugiat adipiscing ut. Lobortis, lobortis vulputate erat laoreet dignissim, qui dolor elit minim blandit tation. Eu at diam augue nostrud ex, tation, wisi, erat luptatum tation adipiscing, in. Consectetuer zzril nisl consequat accumsan tincidunt, feugait suscipit dolore nisl et at. Iusto, nisl nonummy molestie qui vel augue eum iriure vel wisi luptatum, lorem.</p>
  <p class="gap">Iusto dignissim dolore aliquam nulla nibh et velit dolore aliquip consequat wisi ut dolore autem te suscipit volutpat tation. Te praesent eum magna, ipsum elit in consectetuer ut hendrerit exerci zzril tation veniam molestie vero eros enim eu vulputate, ut eros nulla. Euismod exerci, feugait enim minim vero commodo accumsan delenit ut illum sed vero, hendrerit ut suscipit velit vel, ullamcorper aliquip ea. In praesent dolore veniam in odio duis, tincidunt feugait hendrerit iriure ipsum delenit, iriure, odio lobortis veniam, enim. Laoreet facilisi nulla volutpat consequat, qui vel facilisis duis eu veniam duis, facilisi dolor feugiat, aliquip, ad lobortis. Tation augue amet, ut consectetuer nibh nostrud sed commodo esse. Suscipit dolore praesent odio dolore, accumsan, iusto quis facilisis consequat ea eum duis.</p>
</div>
<footer class="abs footer" style="top:2897px"><b>Copyright |</b> All rights reserved</footer>

</body>
</html>
```